Company service wheel graphic

A graphic demonstrating all the services the company offers.
I have hand drawn and written up on the attached the content that is required. Also attached is our company logo so you have a sense of the colour scheme of the logo.
This will eventually go into a company brochure, be used on our website etc.

Target Market(s)

Local GOvernment and other professionals who work in the sport, recreation and leisure industries

Industry/Entity Type

Sports, recreation, leisure, aquatics

Font styles to use
Other font styles liked:
• Calibri

Colors
0054AA
0677BA
7BADD7
CADEEF
E8F1F8

Requirements
Must have
• An eye catching graphic that captures all the information in the hand drawn atachement.
Nice to have
• Each quadrant in the circle to have its own colour, that links to the company logo

```html
<!DOCTYPE html>
<html lang="en">
<head>
<meta charset="utf-8">
<title>Service Wheel</title>
<link rel="stylesheet" href="https://fonts.googleapis.com/css2?family=Montserrat:wght@700;800&family=Roboto:wght@700;900&display=swap">
<style>
  :root {
    --blue: #1076bc;
    --navy: #25215e;
    --label-blue: #1a75bb;
    --white: #ffffff;
    --font-label: "Montserrat", Arial, sans-serif;
    --font-body: "Roboto", Arial, sans-serif;
  }
  html, body {
    margin: 0;
    padding: 0;
    width: 1200px;
    height: 1190px;
    overflow: hidden;
    background: var(--white);
  }
  .wheel {
    display: block;
    width: 1190px;
    height: 1190px;
    margin: 0 auto;
  }
  .segment { stroke: var(--white); stroke-width: 12; }
  .segment--blue { fill: var(--blue); }
  .segment--navy { fill: var(--navy); }
  .ring { fill: var(--blue); stroke: var(--white); stroke-width: 6; }
  .ring-line { fill: none; stroke: var(--white); stroke-width: 5; }
  .divider { stroke: var(--white); stroke-width: 6; }
  .hub { fill: var(--white); }

  .audience {
    font-family: var(--font-label);
    font-weight: 700;
    letter-spacing: 3px;
  }
  .audience--top { fill: var(--label-blue); font-size: 40px; letter-spacing: 2.5px; }
  .audience--bottom { fill: var(--navy); font-size: 44px; }
  .audience--right { letter-spacing: 2px; }

  .ring-title {
    font-family: var(--font-label);
    font-weight: 800;
    fill: var(--white);
    font-size: 23px;
    letter-spacing: 1.5px;
  }
  .stage {
    font-family: var(--font-label);
    font-weight: 700;
    fill: var(--white);
    font-size: 17px;
    letter-spacing: 1.5px;
  }
  .service {
    font-family: var(--font-body);
    font-weight: 700;
    fill: var(--white);
    font-size: 24px;
    letter-spacing: 0.3px;
  }
  .service--small { font-size: 22px; }
  .service--bottom { font-size: 27px; }
  .hub-title {
    font-family: var(--font-body);
    font-weight: 900;
    fill: var(--navy);
    text-anchor: middle;
  }
</style>
</head>
<body>
<svg class="wheel" viewBox="0 0 1930 1930" xmlns="http://www.w3.org/2000/svg" role="img" aria-label="Service wheel: community and stakeholder engagement">
  <defs>
    <path id="arc-audience-top" d="M274,709 A738,738 0 0 1 1656,709"/>
    <path id="arc-audience-left" d="M192,796 A790,790 0 0 0 993,1750"/>
    <path id="arc-audience-right" d="M1075,1742 A790,790 0 0 0 1734,780"/>

    <path id="arc-ring-top" d="M678,856 A305,305 0 0 1 1252,856"/>
    <path id="arc-ring-bottom" d="M712,1172 A330,330 0 0 0 1218,1172"/>

    <path id="arc-stage-planning" d="M813,779 A236,236 0 0 1 1117,779"/>
    <path id="arc-stage-management" d="M1146,808 A236,236 0 0 1 1146,1112"/>
    <path id="arc-stage-growing" d="M761,1078 A236,236 0 0 1 798,793"/>
    <path id="arc-stage-outcome" d="M743,1099 A262,262 0 0 0 1100,1185"/>

    <path id="arc-top-1" d="M483,623 A588,588 0 0 1 1479,675"/>
    <path id="arc-top-2" d="M523,650 A540,540 0 0 1 1437,698"/>
    <path id="arc-top-3" d="M555,673 A500,500 0 0 1 1402,718"/>
    <path id="arc-top-4" d="M582,692 A468,468 0 0 1 1374,733"/>
    <path id="arc-top-5" d="M613,713 A430,430 0 0 1 1341,752"/>

    <path id="arc-right-1" d="M1440,561 A620,620 0 0 1 1275,1497"/>
    <path id="arc-right-2" d="M1408,588 A578,578 0 0 1 1254,1461"/>
    <path id="arc-right-3" d="M1377,614 A538,538 0 0 1 1234,1426"/>
    <path id="arc-right-4" d="M1346,641 A497,497 0 0 1 1214,1390"/>
    <path id="arc-right-5" d="M1315,666 A457,457 0 0 1 1194,1356"/>
    <path id="arc-right-6" d="M1285,691 A418,418 0 0 1 1174,1322"/>

    <path id="arc-left-1" d="M427,1296 A635,635 0 0 1 516,511"/>
    <path id="arc-left-2" d="M463,1274 A592,592 0 0 1 546,541"/>
    <path id="arc-left-3" d="M497,1253 A552,552 0 0 1 575,570"/>
    <path id="arc-left-4" d="M531,1231 A512,512 0 0 1 603,598"/>
    <path id="arc-left-5" d="M565,1210 A472,472 0 0 1 631,626"/>
    <path id="arc-left-6" d="M599,1189 A432,432 0 0 1 660,655"/>
    <path id="arc-left-7" d="M633,1168 A392,392 0 0 1 688,683"/>

    <path id="arc-bottom-1" d="M560,1277 A920,920 0 0 0 1100,1424"/>
    <path id="arc-bottom-2" d="M560,1325 A960,960 0 0 0 1100,1464"/>
    <path id="arc-bottom-3" d="M560,1371 A1000,1000 0 0 0 1100,1504"/>
    <path id="arc-bottom-4" d="M560,1417 A1040,1040 0 0 0 1100,1544"/>
  </defs>

  <!-- Audience labels -->
  <text class="audience audience--top"><textPath href="#arc-audience-top" startOffset="50%" text-anchor="middle">LOCAL &amp; STATE GOVERNMENT . SPORT &amp; LEISURE FACILITY MANAGERS .</textPath></text>
  <text class="audience audience--bottom"><textPath href="#arc-audience-left">INVESTORS, DEVELOPERS, ARCHITECTS &amp; DESIGNERS.</textPath></text>
  <text class="audience audience--bottom audience--right"><textPath href="#arc-audience-right">SPORT, RECREATION &amp; COMMUNITY PROVIDERS</textPath></text>

  <!-- Service segments -->
  <g class="segments">
    <path class="segment segment--blue" d="M465,460 A707,707 0 0 1 1514,515 L1246,732 A362,362 0 0 0 709,704 Z"/>
    <path class="segment segment--navy" d="M1514,515 A707,707 0 0 1 1329,1566 L1151,1270 A362,362 0 0 0 1246,732 Z"/>
    <path class="segment segment--blue" d="M1329,1566 A707,707 0 0 1 366,1335 L658,1152 A362,362 0 0 0 1151,1270 Z"/>
    <path class="segment segment--navy" d="M366,1335 A707,707 0 0 1 465,460 L709,704 A362,362 0 0 0 658,1152 Z"/>
  </g>

  <!-- Core rings -->
  <circle class="ring" cx="965" cy="960" r="360"/>
  <circle class="ring-line" cx="965" cy="960" r="283"/>
  <g class="dividers">
    <line class="divider" x1="816" y1="811" x2="765" y2="760"/>
    <line class="divider" x1="1128" y1="828" x2="1185" y2="782"/>
    <line class="divider" x1="1073" y1="1140" x2="1111" y2="1203"/>
    <line class="divider" x1="787" y1="1071" x2="725" y2="1110"/>
  </g>
  <circle class="hub" cx="965" cy="960" r="208"/>

  <text class="ring-title"><textPath href="#arc-ring-top" startOffset="50%" text-anchor="middle">COMMUNITY, AQUATIC &amp; RECREATION FACILITIES</textPath></text>
  <text class="ring-title"><textPath href="#arc-ring-bottom" startOffset="50%" text-anchor="middle">COMMUNITY ACTIVATION</textPath></text>

  <text class="stage"><textPath href="#arc-stage-planning" startOffset="50%" text-anchor="middle">PLANNING</textPath></text>
  <text class="stage"><textPath href="#arc-stage-management" startOffset="50%" text-anchor="middle">MANAGEMENT</textPath></text>
  <text class="stage"><textPath href="#arc-stage-growing" startOffset="50%" text-anchor="middle">GROWING PARTICIPATION</textPath></text>
  <text class="stage"><textPath href="#arc-stage-outcome" startOffset="50%" text-anchor="middle">COMMUNITY &amp; IMPACT OUTCOME</textPath></text>

  <!-- Hub -->
  <text class="hub-title" x="965" y="905" font-size="44">COMMUNITY</text>
  <text class="hub-title" x="965" y="952" font-size="40">&amp;</text>
  <text class="hub-title" x="967" y="1002" font-size="43">STAKEHOLDER</text>
  <text class="hub-title" x="967" y="1048" font-size="38">ENGAGEMENT</text>

  <!-- Planning services -->
  <g class="services services--planning">
    <text class="service"><textPath href="#arc-top-1" startOffset="50%" text-anchor="middle">. FEACIBILITY STUDIES</textPath></text>
    <text class="service"><textPath href="#arc-top-2" startOffset="50%" text-anchor="middle">. COMMUNITY &amp; STAKEHOLDER RESEARCH</textPath></text>
    <text class="service"><textPath href="#arc-top-3" startOffset="50%" text-anchor="middle">. SPORTS &amp; RECREATION STRATEGIES</textPath></text>
    <text class="service"><textPath href="#arc-top-4" startOffset="50%" text-anchor="middle">. DESIGN STRATEGIES</textPath></text>
    <text class="service"><textPath href="#arc-top-5" startOffset="50%" text-anchor="middle">. INDOOR &amp; OUTDOOR SPACES</textPath></text>
  </g>

  <!-- Management services -->
  <g class="services services--management">
    <text class="service"><textPath href="#arc-right-1" startOffset="52%" text-anchor="middle">. ACTIVATING UNDERUTILIZED ASSETS</textPath></text>
    <text class="service"><textPath href="#arc-right-2" startOffset="50%" text-anchor="middle">. INCOME &amp; REVENUE GENERATION STRATEGIES</textPath></text>
    <text class="service"><textPath href="#arc-right-3" startOffset="48%" text-anchor="middle">. MYSTERY SHOPPER &amp; BUSINESS HEALTH STRATEGIES</textPath></text>
    <text class="service"><textPath href="#arc-right-4" startOffset="50%" text-anchor="middle">. FINANCIAL &amp; FUNDING STRATEGIES</textPath></text>
    <text class="service"><textPath href="#arc-right-5" startOffset="50%" text-anchor="middle">. MANAGEMENT SUPPORT</textPath></text>
    <text class="service"><textPath href="#arc-right-6" startOffset="50%" text-anchor="middle">. BUSINESS PLANNING</textPath></text>
  </g>

  <!-- Growing participation services -->
  <g class="services services--participation">
    <text class="service service--small"><textPath href="#arc-left-1" startOffset="52%" text-anchor="middle">. TRENDS &amp; INSIGHTS</textPath></text>
    <text class="service service--small"><textPath href="#arc-left-2" startOffset="50%" text-anchor="middle">. HEALTH PROFILING</textPath></text>
    <text class="service service--small"><textPath href="#arc-left-3" startOffset="50%" text-anchor="middle">. ACTIVE RECREATION STRATEGIES</textPath></text>
    <text class="service service--small"><textPath href="#arc-left-4" startOffset="50%" text-anchor="middle">. COMMUNITY PROGRAM DEVELOPEMENT</textPath></text>
    <text class="service service--small"><textPath href="#arc-left-5" startOffset="50%" text-anchor="middle">. PHYSICAL ACTIVITY STRATEGIES</textPath></text>
    <text class="service service--small"><textPath href="#arc-left-6" startOffset="50%" text-anchor="middle">. SPECIFIC COHORT STRATEGIES</textPath></text>
    <text class="service service--small"><textPath href="#arc-left-7" startOffset="48%" text-anchor="middle">. SPORT &amp; PROGRAM SPECIFIC STRATEGIES</textPath></text>
  </g>

  <!-- Community activation services -->
  <g class="services services--activation">
    <text class="service service--bottom"><textPath href="#arc-bottom-1" startOffset="180">· CONTRACT MONITORING</textPath></text>
    <text class="service service--bottom"><textPath href="#arc-bottom-2" startOffset="119">· COMMUNITY OUTCOMES &amp; KPIS</textPath></text>
    <text class="service service--bottom"><textPath href="#arc-bottom-3" startOffset="201">· SOCIAL VALUE</textPath></text>
    <text class="service service--bottom"><textPath href="#arc-bottom-4" startOffset="62">· COMMUNITY IMPACT MONITORING</textPath></text>
  </g>
</svg>
</body>
</html>
```